Packaging design - PROTEIN BALLS

PACKAGING
The packaging is a round carton roll, size: Ø73x180 mm, mockup sample enclosed, The label on the carton roll should have a size of 225x178 mm (width x height)

PRODUCT
Chrunchy, cheesy PROTEIN BALLS (100% pure cheese) with a huge amount of protein (65%), a lot of calcium and very low carbogydrates (3%). Diameter about 1.5 cm.

DESIGN
Since our customers are very sporty people, runner, bodybuilder, etc. The design must fit to this sporty customer segment.

FILES
We need the open data for InDesign with all fonts and pictures. If there are licenses tu buy, we will do it.

SUMMARY
1. SNACK
• Crunchy cheese balls with a diameter of about 1.5cm
• 3 different flavors: "Swiss Alpine Salt", "Provencale" and "Hot Chili"
• High in Protein (65%) and Calcium (2%)
• Low in carbohydrates (3%)

2. PACKAGING
• Carton roll, size: Ø73x180 mm
• Background can be every color, but we think a black one will be high premium.
• Maybe different sports are represented in the background, maybe also cheese
• Be creative
• Label applied, size: 225x178 mm

3. DESIGN
• Product name = (Cheese) PROTEIN BALLS
• 3 different colors for the 3 flavors "Swiss Alpine Salt", "Provencale" and "Hot Chili"
• HighProtein, High Calcium and LowCarb must be pointed out on the front
• Swissness: Swiss made must be pointed out
• fresh and young design, most customers are sporty people, pumper with a strong body awareness

TARGET CUSTOMER
Our main customers are extremely sporty people, who work very hard on their muscles and fitness, most of them are runners, cross fitnesser, bodybuilders, etc We will launch the product in fitness centers, in supplement shops and we are planning to make some stories with sporty influencer.

Serif
Sans Serif

• Cheese, naturalness, healthy, PROTEIN balls, muscles, Swissness must showed on the product.

```html
<!DOCTYPE html>
<html lang="en">
<head>
<meta charset="UTF-8">
<title>Protein Balls – Swiss Alpine Salt label</title>
<link rel="stylesheet" href="https://fonts.googleapis.com/css2?family=Kanit:wght@500;600&display=swap">
<style>
  :root {
    --bg: #000000;
    --bg-glow: #262626;
    --blue: #0b4fa0;
    --blue-deep: #062a5c;
    --blue-light: #3d7fd6;
    --shield-face: #1c1c1c;
    --white: #ffffff;
    --title-low: #c4c4c4;
    --cheese: #d8cf9a;
  }
  * { margin: 0; padding: 0; box-sizing: border-box; }
  html, body { width: 1200px; height: 953px; overflow: hidden; background: var(--bg); }
  .label {
    position: relative;
    width: 1200px;
    height: 953px;
    overflow: hidden;
    background: radial-gradient(ellipse 520px 420px at 470px 300px, var(--bg-glow), var(--bg) 75%);
  }
  .swoosh { position: absolute; inset: 0; }
  .athlete-photo {
    position: absolute;
    left: 134px; top: 71px;
    width: 642px; height: 882px;
    background: radial-gradient(ellipse 60% 45% at 55% 28%, rgba(29,111,209,.9) 0%, rgba(18,74,143,.6) 45%, rgba(30,30,30,.4) 75%, rgba(0,0,0,0) 100%);
  }
  .product-name {
    position: absolute;
    left: 138px;
    font-family: "Kanit", sans-serif;
    font-weight: 600;
    font-size: 150px;
    line-height: 1;
    letter-spacing: 0;
    text-transform: uppercase;
  }
  .product-name--top { top: 340px; color: var(--white); }
  .product-name--bottom { top: 492px; color: var(--title-low); }
  .product-photo {
    position: absolute;
    left: 660px; top: 515px;
    width: 120px; height: 127px;
    border-radius: 45% 48% 44% 50%;
    background: radial-gradient(circle at 40% 35%, #f0e8bd, var(--cheese) 55%, #a99d62);
  }
  .flavour-band {
    position: absolute;
    left: 303px; top: 673px;
    width: 482px; height: 84px;
    background: linear-gradient(90deg, rgba(11,79,160,0) 0%, var(--blue) 30%, var(--blue) 100%);
    clip-path: polygon(0 0, 100% 0, 96% 100%, 0 100%);
    border-bottom: 2px solid var(--blue-light);
  }
  .flavour-name {
    position: absolute;
    left: 361px; top: 684px;
    font-family: "Kanit", sans-serif;
    font-weight: 500;
    font-size: 44px;
    line-height: 60px;
    color: var(--white);
  }
  .claim {
    position: absolute;
    left: 905px;
    width: 205px; height: 223px;
  }
  .claim svg { position: absolute; inset: 0; }
  .claim-text {
    position: absolute;
    inset: 0 0 18px 0;
    display: flex; flex-direction: column; align-items: center; justify-content: center;
    font-family: "Kanit", sans-serif;
    font-weight: 500;
    color: var(--white);
    text-align: center;
    font-size: 27px;
    line-height: 1.05;
  }
  .claim-value { font-size: 40px; line-height: 1.2; margin-top: 2px; }
  .claim--protein { top: 138px; }
  .claim--calcium { top: 383px; }
  .claim--carbs { top: 628px; }
</style>
</head>
<body>
<main class="label">
  <svg class="swoosh" width="1200" height="953" viewBox="0 0 1200 953" aria-hidden="true">
    <defs>
      <linearGradient id="bandFill" x1="0" y1="0" x2="1" y2="0">
        <stop offset="0" stop-color="#062a5c"/>
        <stop offset=".55" stop-color="#0b4fa0"/>
        <stop offset="1" stop-color="#0d3f80"/>
      </linearGradient>
      <linearGradient id="bandFade" x1="0" y1="0" x2="0" y2="1">
        <stop offset="0" stop-color="#000" stop-opacity="0"/>
        <stop offset="1" stop-color="#000" stop-opacity=".85"/>
      </linearGradient>
    </defs>
    <path d="M0,725 C350,840 800,830 1200,395 L1200,640 C850,860 400,880 0,800 Z" fill="url(#bandFill)"/>
    <path d="M0,725 C350,840 800,830 1200,395 L1200,640 C850,860 400,880 0,800 Z" fill="url(#bandFade)" opacity=".5"/>
    <path d="M0,725 C350,840 800,830 1200,395" fill="none" stroke="#1f5fb4" stroke-width="2"/>
    <ellipse cx="560" cy="805" rx="90" ry="6" fill="#ffffff" opacity=".35"/>
  </svg>

  <div class="athlete-photo" role="img" aria-label="Photo of a sprinting athlete in a blue shirt and dark shorts"></div>

  <h1 class="product-name product-name--top">Protein</h1>
  <p class="product-name product-name--bottom">Balls</p>

  <div class="product-photo" role="img" aria-label="Photo of a single crunchy cheese protein ball"></div>

  <div class="flavour-band"></div>
  <p class="flavour-name">Swiss Alpine Salt</p>

  <div class="claim claim--protein">
    <svg viewBox="0 0 205 223" width="205" height="223" aria-hidden="true">
      <path d="M8,22 L102,4 L197,22 L190,140 L102,219 L15,140 Z" fill="#cfcfcf" stroke="#777" stroke-width="2"/>
      <path d="M20,32 L102,17 L185,32 L179,134 L102,203 L26,134 Z" fill="var(--shield-face)" stroke="#555" stroke-width="2"/>
    </svg>
    <div class="claim-text"><span>High in</span><span>Protein</span><span class="claim-value">(65%)</span></div>
  </div>

  <div class="claim claim--calcium">
    <svg viewBox="0 0 205 223" width="205" height="223" aria-hidden="true">
      <path d="M8,22 L102,4 L197,22 L190,140 L102,219 L15,140 Z" fill="#cfcfcf" stroke="#777" stroke-width="2"/>
      <path d="M20,32 L102,17 L185,32 L179,134 L102,203 L26,134 Z" fill="var(--shield-face)" stroke="#555" stroke-width="2"/>
    </svg>
    <div class="claim-text"><span>Calcium</span><span class="claim-value">(2%)</span></div>
  </div>

  <div class="claim claim--carbs">
    <svg viewBox="0 0 205 223" width="205" height="223" aria-hidden="true">
      <path d="M8,22 L102,4 L197,22 L190,140 L102,219 L15,140 Z" fill="#cfcfcf" stroke="#777" stroke-width="2"/>
      <path d="M20,32 L102,17 L185,32 L179,134 L102,203 L26,134 Z" fill="var(--shield-face)" stroke="#555" stroke-width="2"/>
    </svg>
    <div class="claim-text"><span>Low in</span><span>carboh-</span><span>ydrates</span><span class="claim-value">(3%)</span></div>
  </div>
</main>
</body>
</html>
```